Vesna Architecture

We are a architectural design and build company working between scales 1/1000 to 1/1 we want people to understand our difference from our design experience and quality.we build hotels restourants and office spaces.Our company name is Vesna architecture to mind sustainability.

We want to write our adress phone and work spesifications on the card and we want our logo as backround.

Ps:you could find the logo adress and phone box numbers from the web:www.vesnayapi.example

Target Market(s)

Who looks for experts.

Industry/Entity Type

Architecture

Requirements
Must have
• Design is over everything.
Should not have
• we don want it to be colorfull

```html
<!DOCTYPE html>
<html lang="en">
<head>
<meta charset="utf-8">
<title>Vesna Architecture – Business Card</title>
<link rel="stylesheet" href="https://fonts.googleapis.com/css2?family=Source+Sans+3:wght@300;400;600;700&display=swap">
<style>
  :root {
    --page: #ecebe8;
    --paper: #ffffff;
    --ink: #231f20;
    --teal: #0f4b5b;
    --teal-soft: #1c5c6b;
    --steel: #a9c2d6;
    --light: #ffffff;
    --logo-grey: #8a8478;
  }
  * { box-sizing: border-box; margin: 0; padding: 0; }
  html, body { width: 1200px; height: 1200px; overflow: hidden; }
  body {
    background: var(--page);
    font-family: "Source Sans 3", sans-serif;
    position: relative;
  }
  .card {
    position: absolute;
    width: 620px;
    height: 616px;
    background: var(--paper);
    box-shadow: 4px 5px 10px rgba(0,0,0,0.25);
    overflow: hidden;
  }
  .card--front { left: 42px; top: 63px; z-index: 2; }
  .card--back { left: 524px; top: 500px; z-index: 1; }

  .front__top { height: 237px; display: flex; align-items: center; justify-content: center; gap: 12px; }
  .brand-dot { width: 16px; height: 16px; border-radius: 50%; background: var(--logo-grey); }
  .brand-name { font-size: 30px; font-weight: 300; color: var(--logo-grey); letter-spacing: 2px; }

  .front__bottom {
    height: 379px;
    background: var(--ink);
    color: var(--light);
    text-align: center;
    position: relative;
  }
  .person { position: absolute; top: 182px; width: 100%; }
  .person__name { font-size: 18px; font-weight: 700; letter-spacing: 0.5px; }
  .person__role { font-size: 12px; font-weight: 400; margin-top: 2px; }
  .address { position: absolute; top: 268px; width: 100%; }
  .address__street { font-size: 16px; font-weight: 700; color: var(--steel); letter-spacing: 0.3px; }
  .address__city { font-size: 13px; margin-top: 4px; }
  .contacts {
    position: absolute; top: 352px; left: 46px; right: 44px;
    display: flex; justify-content: space-between;
    font-size: 13px;
  }
  .contacts b { font-weight: 700; margin-right: 10px; }

  .back__top { height: 240px; position: relative; }
  .back__mark {
    position: absolute; left: 0; right: 0; top: 40px;
    text-align: center; transform: rotate(180deg);
    color: var(--ink);
  }
  .back__mark .brand-name { color: var(--ink); font-size: 84px; line-height: 1; display: block; letter-spacing: 5px; }
  .back__mark .brand-sub { font-size: 16px; letter-spacing: 4px; display: block; margin-top: 4px; }

  .back__bottom {
    height: 376px; position: relative;
    background: linear-gradient(180deg, var(--teal) 0%, var(--teal-soft) 50%, var(--teal) 100%);
  }
  .back__bottom-mark {
    position: absolute; left: 0; right: 0; top: 150px;
    text-align: center; color: var(--light);
  }
  .back__bottom-mark .brand-name { color: var(--light); font-size: 52px; display: block; letter-spacing: 3px; }
  .back__bottom-mark .brand-sub { font-size: 13px; letter-spacing: 3px; display: block; margin-top: -2px; }
</style>
</head>
<body>
  <section class="card card--front">
    <div class="front__top">
      <span class="brand-dot"></span>
      <span class="brand-name">vesna</span>
    </div>
    <div class="front__bottom">
      <div class="person">
        <p class="person__name">NAME</p>
        <p class="person__role">Managing Director</p>
      </div>
      <div class="address">
        <p class="address__street">Ihlamur Mah. Lale Cad, Papatya Sok.</p>
        <p class="address__city">No. 24 Kuzguncuk Uskudar/istanbul</p>
      </div>
      <div class="contacts">
        <span><b>t.</b>0216 555 01 47</span>
        <span><b>f.</b>0216 555 01 48</span>
        <span><b>e.</b>vesnayapi@example.com</span>
      </div>
    </div>
  </section>

  <section class="card card--back">
    <div class="back__top">
      <div class="back__mark">
        <span class="brand-name">vesna</span>
        <span class="brand-sub">MİMARLIK</span>
      </div>
    </div>
    <div class="back__bottom" role="img" aria-label="Repeating background pattern of the Vesna brand mark in a lighter teal">
      <div class="back__bottom-mark">
        <span class="brand-name">vesna</span>
        <span class="brand-sub">MİMARLIK</span>
      </div>
    </div>
  </section>
</body>
</html>
```